Design a PowerPoint template for a consultancy organisation

I am after a Powerpoint template including three pages a title slide (that should have a title and subtitle), A title and content slide and a section header slide. I expect the company name and/or logo to be prominent and the colors to work well with the logo colors. I have included a copy of the logo

```html
<!DOCTYPE html>
<html lang="en">
<head>
<meta charset="utf-8">
<title>Parley Works – Presentation Template</title>
<link rel="stylesheet" href="https://fonts.googleapis.com/css2?family=Montserrat:wght@300;400;500;600;700;800&display=swap">
<style>
  :root {
    --green: #8dc63f;
    --purple: #6a12b0;
    --ink: #1f1f1f;
    --body: #3a3a3a;
    --muted: #8a8a8a;
    --rule: #d6d6d6;
    --stage: #a9a9a9;
    --white: #ffffff;
  }
  * { box-sizing: border-box; margin: 0; padding: 0; }
  html, body { width: 1200px; height: 685px; overflow: hidden; background: var(--stage); }
  body { font-family: "Montserrat", sans-serif; color: var(--ink); }

  .deck {
    position: relative; width: 1200px; height: 685px; padding: 8px;
    display: grid; grid-template-columns: 589px 589px; grid-template-rows: 331px 331px; gap: 6px;
  }
  .slide { position: relative; overflow: hidden; background: var(--white); }

  /* brand wordmark */
  .brand { display: flex; align-items: center; gap: 5px; color: var(--purple); font-weight: 600; white-space: nowrap; }
  .brand-dot { width: 0.8em; height: 0.8em; background: var(--green); }

  /* photo areas */
  .photo {
    position: absolute; inset: 0;
    background:
      linear-gradient(90deg, rgba(255,255,255,0.97) 0%, rgba(255,255,255,0.85) 30%, rgba(255,255,255,0.35) 60%, rgba(255,255,255,0.15) 100%),
      linear-gradient(135deg, #c9b9a8 0%, #b59c86 35%, #8f8a86 60%, #c7c2bd 100%);
  }

  /* title slide */
  .title-slide .brand { position: absolute; left: 37px; top: 98px; font-size: 19px; }
  .title-slide .headline { position: absolute; left: 37px; top: 152px; }
  .title-slide .headline-main { font-weight: 800; font-size: 27px; line-height: 1; letter-spacing: -0.3px; }
  .title-slide .headline-second { font-weight: 800; font-size: 20px; line-height: 1.1; letter-spacing: -0.3px; margin-left: 2px; }
  .title-slide .subtitle { color: var(--purple); font-weight: 600; font-size: 13.5px; margin-top: 3px; }
  .presenter {
    position: absolute; left: 40px; top: 266px; width: 98px; height: 23px; border-radius: 12px;
    background: var(--green); color: var(--white); font-size: 7px; display: flex; align-items: center; justify-content: center;
  }

  /* content slides */
  .header-band {
    position: absolute; left: 0; top: 0; width: 100%; height: 56px; color: var(--white); text-align: center;
    padding-top: 11px; box-shadow: 0 3px 6px rgba(0,0,0,0.08);
  }
  .header-band .pointer { position: absolute; left: 50%; bottom: -9px; transform: translateX(-50%); width: 20px; height: 10px; }
  .content-slide.green .header-band { background: var(--green); }
  .content-slide.purple .header-band { background: var(--purple); }
  .header-title { font-weight: 700; font-size: 19px; letter-spacing: -0.5px; line-height: 1.05; }
  .header-sub { font-weight: 400; font-size: 10.5px; letter-spacing: 3px; margin-top: 1px; }

  .body-copy { position: absolute; left: 38px; top: 99px; width: 504px; }
  .body-copy p { font-size: 7.2px; line-height: 1.25; color: var(--body); text-align: justify; margin-bottom: 13px; }
  .body-copy p.tight { margin-bottom: 4px; }

  .footer { position: absolute; left: 24px; right: 22px; top: 306px; border-top: 1px solid var(--rule); height: 22px; }
  .footer .accent { position: absolute; left: 50%; top: -4px; margin-left: -17px; width: 34px; height: 4px; }
  .content-slide.green .footer .accent { background: var(--purple); }
  .content-slide.purple .footer .accent { background: var(--green); }
  .footer .copyright { position: absolute; left: 4px; top: 8px; font-size: 5.5px; color: var(--muted); }
  .footer .page { position: absolute; left: 50%; top: 8px; transform: translateX(-50%); font-size: 6px; color: var(--ink); }
  .footer .brand { position: absolute; right: 0; top: 5px; font-size: 8px; }

  /* section slide */
  .section-slide .brand { position: absolute; left: 40px; top: 100px; font-size: 10px; }
  .section-slide .section-title { position: absolute; left: 40px; top: 140px; }
  .section-title-main { font-weight: 700; font-size: 25px; line-height: 1; letter-spacing: -0.2px; }
  .section-title-sub { color: var(--purple); font-weight: 600; font-size: 20px; line-height: 1.2; }
  .section-slide .section-copy { position: absolute; left: 37px; top: 206px; width: 265px; font-size: 7.2px; line-height: 1.25; color: var(--body); }
</style>
</head>
<body>
<main class="deck">

  <section class="slide title-slide">
    <div class="photo" role="img" aria-label="Overhead photo of colleagues working at a shared wooden table with laptops, faded to white on the left"></div>
    <div class="brand"><span class="brand-dot"></span>Parley Works</div>
    <div class="headline">
      <h1 class="headline-main">PRESENTATION</h1>
      <div class="headline-second">TITLE GOES HERE</div>
      <div class="subtitle">Sub Title Goes Here</div>
    </div>
    <div class="presenter">Presenter Name</div>
  </section>

  <section class="slide content-slide green">
    <header class="header-band">
      <h2 class="header-title">ADD AWESOME TITLE HERE</h2>
      <div class="header-sub">SUB TITLE GOES HERE</div>
      <svg class="pointer" viewBox="0 0 20 10"><polygon points="0,0 20,0 10,10" fill="var(--green)"/></svg>
    </header>
    <div class="body-copy">
      <p>Lorem ipsum dolor sit amet, consectetur adipiscing elit, sed do eiusmod tempor incididunt ut labore et dolore magna aliqua. Lorem ipsum dolor sit amet, consectetur adipiscing elit, sed do eiusmod tempor incididunt ut labore et dolore magna aliqua. Ut enim ad minim veniam, quis nostrud exercitation ullamco laboris nisi ut aliquip.</p>
      <p>Lorem ipsum dolor sit amet, consectetur adipiscing elit, Lorem ipsum dolor sit amet, consectetur adipiscing elit, sed do eiusmod tempor incididunt ut labore et dolore magna aliqua. Lorem ipsum dolor sit amet, consectetur adipiscing elit, sed do eiusmod tempor incididunt ut labore et dolore magna aliqua. Ut enim ad minim veniam, quis nostrud exercitation ullamco laboris nisi ut aliquip.</p>
      <p class="tight">Lorem ipsum dolor sit amet, consectetur adipiscing elit, sed do eiusmod tempor incididunt ut labore et dolore magna aliqua. Lorem ipsum dolor sit amet, consectetur adipiscing elit, sed do eiusmod tempor incididunt ut labore et dolore magna aliqua.</p>
      <p>sed do eiusmod tempor incididunt ut labore et dolore magna aliqua. Lorem ipsum dolor sit amet, consectetur adipiscing elit, sed do eiusmod tempor incididunt ut labore et dolore magna aliqua. Lorem ipsum dolor sit amet, consectetur adipiscing elit, sed do eiusmod tempor incididunt ut labore et dolore magna aliqua. Lorem ipsum dolor sit amet, consectetur adipiscing elit, sed do eiusmod tempor incididunt ut labore et dolore magna aliqua. Ut enim ad minim veniam, quis nostrud exercitation ullamco laboris nisi ut aliquip.</p>
      <p>Lorem ipsum dolor sit amet, consectetur adipiscing elit, sed do eiusmod tempor incididunt ut labore et dolore magna aliqua. Lorem ipsum dolor sit amet, consectetur adipiscing elit, sed do eiusmod tempor incididunt ut labore et dolore magna aliqua.</p>
    </div>
    <footer class="footer">
      <span class="accent"></span>
      <span class="copyright">Copyright © | All Rights Reserved</span>
      <span class="page">7</span>
      <span class="brand">Parley Works</span>
    </footer>
  </section>

  <section class="slide content-slide purple">
    <header class="header-band">
      <h2 class="header-title">ADD AWESOME TITLE HERE</h2>
      <div class="header-sub">SUB TITLE GOES HERE</div>
      <svg class="pointer" viewBox="0 0 20 10"><polygon points="0,0 20,0 10,10" fill="var(--purple)"/></svg>
    </header>
    <div class="body-copy">
      <p>Lorem ipsum dolor sit amet, consectetur adipiscing elit, sed do eiusmod tempor incididunt ut labore et dolore magna aliqua. Lorem ipsum dolor sit amet, consectetur adipiscing elit, sed do eiusmod tempor incididunt ut labore et dolore magna aliqua. Ut enim ad minim veniam, quis nostrud exercitation ullamco laboris nisi ut aliquip.</p>
      <p>Lorem ipsum dolor sit amet, consectetur adipiscing elit, Lorem ipsum dolor sit amet, consectetur adipiscing elit, sed do eiusmod tempor incididunt ut labore et dolore magna aliqua. Lorem ipsum dolor sit amet, consectetur adipiscing elit, sed do eiusmod tempor incididunt ut labore et dolore magna aliqua. Ut enim ad minim veniam, quis nostrud exercitation ullamco laboris nisi ut aliquip.</p>
      <p class="tight">Lorem ipsum dolor sit amet, consectetur adipiscing elit, sed do eiusmod tempor incididunt ut labore et dolore magna aliqua. Lorem ipsum dolor sit amet, consectetur adipiscing elit, sed do eiusmod tempor incididunt ut labore et dolore magna aliqua.</p>
      <p>sed do eiusmod tempor incididunt ut labore et dolore magna aliqua. Lorem ipsum dolor sit amet, consectetur adipiscing elit, sed do eiusmod tempor incididunt ut labore et dolore magna aliqua. Lorem ipsum dolor sit amet, consectetur adipiscing elit, sed do eiusmod tempor incididunt ut labore et dolore magna aliqua. Lorem ipsum dolor sit amet, consectetur adipiscing elit, sed do eiusmod tempor incididunt ut labore et dolore magna aliqua. Ut enim ad minim veniam, quis nostrud exercitation ullamco laboris nisi ut aliquip.</p>
      <p>Lorem ipsum dolor sit amet, consectetur adipiscing elit, sed do eiusmod tempor incididunt ut labore et dolore magna aliqua. Lorem ipsum dolor sit amet, consectetur adipiscing elit, sed do eiusmod tempor incididunt ut labore et dolore magna aliqua.</p>
    </div>
    <footer class="footer">
      <span class="accent"></span>
      <span class="copyright">Copyright © | All Rights Reserved</span>
      <span class="page">8</span>
      <span class="brand">Parley Works</span>
    </footer>
  </section>

  <section class="slide section-slide">
    <div class="photo" role="img" aria-label="Overhead photo of colleagues working at a shared wooden table with laptops, faded to white on the left"></div>
    <div class="brand"><span class="brand-dot"></span>Parley Works</div>
    <div class="section-title">
      <h2 class="section-title-main">SECTION HEADER</h2>
      <div class="section-title-sub">Title here</div>
    </div>
    <p class="section-copy">Lorem ipsum dolor sit amet, consectetur adipiscing elit, sed do eiusmod tempor incididunt ut labore et dolore magna aliqua. Lorem ipsum dolor sit amet, consectetur adipiscing elit, sed do eiusmod tempor incididunt ut labore et dolore magna aliqua. Ut enim ad minim veniam, quis nostrud exercitation ullamco laboris nisi ut aliquip.</p>
  </section>

</main>
</body>
</html>
```